Spiritual journeyer, astrologer, Reiki master, underground music lover needs business card design

Initially I need a business card design (and possibly a logo for my new website). I offer astrological and energetic inquiry and guidance to clients in support of their life's evolutionary path. I combine an eclectic mix of methods with a focus on the mind body connection. I am a spiritual journeyer, astrologer, Reiki Master, certified personal trainer, soon to be black belt in Taekwondo (karate), and researcher into the benefits of music/sound vibrational therapy. And underground music lover :) The attached drawing is just something I drew freehand, it is symbolic of many things important to me. I wanted the figure to clearly be female. Her arms are open to catch the sky, the name of my new business is Orlabrook, and Orla is my daughter's name. This was just an idea I had, I'm open to suggestions. The photo is me with the planets in the sky as they were at the moment I was born (some years ago-LOL)
Updates

I have picked a final design. Thank you everyone for your time and effort.

Target Market(s)

Worldwide, what I do can be done in person or anywhere in the world via Skype

Industry/Entity Type

Professional Service

Contact Information for Business Card

Simple, unusual image with my business name and contact info

Font styles to use
Sans Serif

Requirements
Must have
• My website very clean, simple. Somehow combine biz name of Orlabrook with female figure catching/holding the starry sky? See my poor drawing I attached.
Nice to have
• Something that conveys all the unique, unusual, eclectic skills and capacities I have
Should not have
• Frilly, fancy, stuffy

```html
<!DOCTYPE html>
<html lang="en">
<head>
<meta charset="utf-8">
<title>Orlabrook Business Card</title>
<link href="https://fonts.googleapis.com/css2?family=Open+Sans:wght@400;600&display=swap" rel="stylesheet">
<style>
  :root{
    --page:#e9e9ec;
    --night:#0c0c26;
    --sky-deep:#1d2fb8;
    --sky-mid:#3b6fe6;
    --sky-glow:#8fd0ff;
    --band:#2b3ad6;
    --accent:#f7941d;
    --ink-light:#ffffff;
    --logo-ink:#0e1030;
  }
  html,body{margin:0;padding:0;width:1200px;height:1200px;overflow:hidden;background:var(--page);}
  body{position:relative;font-family:"Open Sans",Arial,sans-serif;}
  .card{
    position:absolute;left:150px;top:343px;width:900px;height:514px;
    background:var(--night);overflow:hidden;
    box-shadow:0 8px 24px rgba(0,0,0,.25);
  }
  .card__art{position:absolute;inset:0;width:100%;height:100%;}
  .brand-name{
    position:absolute;left:330px;top:150px;margin:0;
    font-size:54px;font-weight:600;color:var(--logo-ink);letter-spacing:.5px;
    transform:rotate(8deg);transform-origin:left center;
  }
  .holder{position:absolute;left:70px;top:268px;width:300px;text-align:right;}
  .holder__name{margin:0;font-size:32px;font-weight:600;color:var(--accent);letter-spacing:.5px;white-space:nowrap;}
  .holder__role{margin:10px 0 0;font-size:17px;line-height:24px;color:var(--ink-light);}
  .divider{position:absolute;left:392px;top:330px;width:1px;height:130px;background:rgba(255,255,255,.35);}
  .contact{position:absolute;left:412px;top:345px;margin:0;padding:0;list-style:none;}
  .contact__item{display:flex;align-items:center;gap:12px;height:30px;font-size:19px;color:var(--ink-light);}
  .contact__icon{width:20px;height:20px;flex:none;}
</style>
</head>
<body>
  <main class="card">
    <svg class="card__art" viewBox="0 0 900 514" aria-hidden="false">
      <defs>
        <radialGradient id="skyGlow" cx="0.55" cy="0.95" r="0.8">
          <stop offset="0" stop-color="var(--sky-glow)"/>
          <stop offset="0.45" stop-color="var(--sky-mid)"/>
          <stop offset="1" stop-color="var(--sky-deep)"/>
        </radialGradient>
        <linearGradient id="nightFade" x1="0" y1="0" x2="0" y2="1">
          <stop offset="0" stop-color="#1a1a44"/>
          <stop offset="1" stop-color="#08081c"/>
        </linearGradient>
      </defs>
      <rect width="900" height="514" fill="url(#nightFade)" role="img" aria-label="Night sky with faint zodiac constellation figures"/>
      <path d="M0 0 H900 V300 C700 280 420 250 0 130 Z" fill="url(#skyGlow)" role="img" aria-label="Glowing starry blue sky"/>
      <path d="M0 130 C420 250 700 280 900 300 L900 312 C700 292 420 262 0 146 Z" fill="var(--band)"/>
    </svg>

    <h1 class="brand-name">Orlabrook</h1>

    <section class="holder">
      <h2 class="holder__name">MARISA HOLLIN</h2>
      <p class="holder__role">Astrological and Energetic<br>Guidance and Inquiry</p>
    </section>

    <div class="divider"></div>

    <ul class="contact">
      <li class="contact__item">
        <svg class="contact__icon" viewBox="0 0 20 20"><circle cx="10" cy="10" r="10" fill="var(--accent)"/><path d="M6.5 5.5l2 0 .8 2.4-1.2.9a6 6 0 0 0 2.8 2.8l.9-1.2 2.4.8v2a1 1 0 0 1-1 1A8 8 0 0 1 5.5 6.5a1 1 0 0 1 1-1z" fill="var(--night)"/></svg>
        555-013-2749
      </li>
      <li class="contact__item">
        <svg class="contact__icon" viewBox="0 0 20 20"><circle cx="10" cy="10" r="10" fill="var(--accent)"/><rect x="5" y="6.5" width="10" height="7" fill="none" stroke="var(--night)" stroke-width="1.4"/><path d="M5 6.5l5 4 5-4" fill="none" stroke="var(--night)" stroke-width="1.4"/></svg>
        email@orlabrook.com
      </li>
      <li class="contact__item">
        <svg class="contact__icon" viewBox="0 0 20 20"><circle cx="10" cy="10" r="10" fill="var(--accent)"/><g fill="none" stroke="var(--night)" stroke-width="1.2"><circle cx="10" cy="10" r="5.5"/><ellipse cx="10" cy="10" rx="2.4" ry="5.5"/><path d="M4.5 10h11"/></g></svg>
        www.orlabrook.com
      </li>
    </ul>
  </main>
</body>
</html>
```